Business Card Design

Very plain simple card, Plain modern font. Background. Grey fading to black. Large Bright lime green text. Saying.

TWR-ZA.COM

Small other details in white text.

Irish Horse Sales . Livery . Stud . Shows

Mark Dabrowski
TWR
Birch Lodge
Carrowmede Lane
Thistlecombe
Lincolnshire
LN4 7JX

Email. Twrzap@mailvale.co.uk
Tel. 07482 936504

Industry/Entity Type

Business

Contact Information for Business Card

As below

```html
<!DOCTYPE html>
<html lang="en">
<head>
<meta charset="utf-8">
<title>TWR-ZA.COM Business Card</title>
<link rel="stylesheet" href="https://fonts.googleapis.com/css2?family=Open+Sans:wght@500&family=Cinzel:wght@400&family=Arimo:wght@400&family=Montserrat:wght@600&display=swap">
<style>
  :root {
    --bg-top: #434343;
    --bg-bottom: #070707;
    --lime: #4cb748;
    --white: #ffffff;
  }
  html, body {
    margin: 0;
    padding: 0;
    width: 1200px;
    height: 791px;
    overflow: hidden;
    background: var(--bg-bottom);
  }
  .card {
    display: block;
    width: 1200px;
    height: 791px;
  }
  .brand {
    font-family: "Open Sans", sans-serif;
    font-weight: 500;
    font-size: 134px;
    fill: var(--lime);
  }
  .tagline {
    font-family: "Cinzel", serif;
    font-size: 40px;
    fill: var(--white);
  }
  .owner {
    font-family: "Arimo", sans-serif;
    font-size: 58px;
    fill: var(--lime);
  }
  .site-name {
    font-family: "Montserrat", sans-serif;
    font-weight: 600;
    font-size: 30px;
    letter-spacing: 1px;
    fill: var(--white);
  }
  .address, .contact {
    font-family: "Arimo", sans-serif;
    font-size: 41px;
    fill: var(--white);
  }
  .divider { stroke: var(--white); stroke-width: 2; }
  .icon-fill { fill: var(--white); }
  .icon-line { fill: none; stroke: #8a8a8a; stroke-width: 1.5; }
</style>
</head>
<body>
<svg class="card" viewBox="0 0 1200 791" xmlns="http://www.w3.org/2000/svg">
  <defs>
    <linearGradient id="card-bg" x1="0" y1="0" x2="0" y2="1">
      <stop offset="0" stop-color="var(--bg-top)"/>
      <stop offset="1" stop-color="var(--bg-bottom)"/>
    </linearGradient>
  </defs>
  <rect width="1200" height="791" fill="url(#card-bg)"/>

  <text class="brand" x="136" y="199" textLength="920" lengthAdjust="spacingAndGlyphs">TWR-ZA.COM</text>
  <text class="tagline" x="137" y="254" textLength="924" lengthAdjust="spacing">IRISH HORSE SALES . LIVERY . STUD . SHOWS</text>
  <text class="owner" x="127" y="343">MARK DABROWSKI&#160; I&#160; TWR</text>

  <g text-anchor="end">
    <text class="site-name" x="468" y="458">BIRCH LODGE</text>
    <text class="address" x="463" y="524">Carrowmede Lane</text>
    <text class="address" x="463" y="576">Thistlecombe</text>
    <text class="address" x="463" y="628">Lincolnshire</text>
    <text class="address" x="463" y="680">LN4 7JX</text>
  </g>

  <line class="divider" x1="541" y1="430" x2="541" y2="695"/>

  <g class="email-icon">
    <rect class="icon-fill" x="600" y="483" width="55" height="34"/>
    <polyline class="icon-line" points="601,484 627.5,504 654,484"/>
  </g>
  <text class="contact" x="686" y="515">Twrzap@mailvale.co.uk</text>

  <path class="icon-fill" d="M621 586 c4-3 7-2 9 1 l6 10 c2 3 1 6-2 8 l-4 3 c3 7 8 13 15 17 l3-4 c2-3 5-3 8-1 l9 7 c3 2 3 5 0 8 l-4 4 c-5 4-13 3-22-3 c-11-8-20-19-25-31 c-3-8-2-15 2-18 z"/>
  <text class="contact" x="686" y="619">07482 936504</text>
</svg>
</body>
</html>
```